Book covers for a 3 book series International Consultancy

We need book covers for our dangerous goods handbook series.

The 3 handbooks are for:
Shippers (Companies that ship dangerous goods)
Carriers (Companies that transport dangerous goods)
Tank (Companies that transport liquid dangerous goods)

Each cover should reflect the function the user of the book carries out.
Each cover should reflect that it is a part of a series (one customer could need all 3 books and needs to be able to tell them apart.

Each cover consists of and requires

Front:
1) Cover (Logo, name of company, name of book, version of book)
2) Front "flip out" (Text area & logo)

Back:
1) Back (ISBN bar code, 2 smaller logos (environmental, will be provided), company info (full name, address, phone, fax, email, web and VAT no)
2) Area to describe what we do = Chemical Compliance Consultancy (please contact me at mikkel.halvorsen@dk.tessanorlab.com) for further material on what we do. We would like to see our icons (attached) in use to describe what we do.

Attached:
- Guidelines (3 separate files)
- Iconography
- Previous Cover

Hi all, Just a kind reminder about the end of the project: the dealine is wednesday. The earlier you submit your designs the better chances you'll have. Looking forward to seeing you great designs. Have a great monday. Stay caffeinated! ;) Best regards, Mikkel

```html
<!DOCTYPE html>
<html lang="en">
<head>
<meta charset="utf-8">
<title>Dangerous Goods Tank – Handbook Cover</title>
<link rel="stylesheet" href="https://fonts.googleapis.com/css2?family=Raleway:ital,wght@0,300;0,700;1,700&family=Open+Sans:ital,wght@1,700&display=swap">
<style>
  :root {
    --green: #1f8a44;
    --green-deep: #0f5a2a;
    --green-dark: #0b4220;
    --paper: #ffffff;
    --backdrop: #e9e6e1;
    --ink-grey: #5a5a5a;
    --steel: #9aa3a8;
    --brick: #9c2a22;
  }
  * { margin: 0; padding: 0; box-sizing: border-box; }
  html, body {
    width: 1200px; height: 960px; overflow: hidden;
    background: var(--backdrop);
  }
  .canvas { position: relative; width: 1200px; height: 960px; }
  .cover {
    position: absolute; left: 280px; top: 49px;
    width: 640px; height: 862px;
    background: var(--paper);
    box-shadow: 0 6px 24px rgba(0,0,0,.18);
  }
  .cover svg { display: block; width: 100%; height: 100%; }
  .series-label { font-family: "Raleway", sans-serif; font-weight: 300; fill: #fff; letter-spacing: .5px; }
  .book-title { font-family: "Raleway", sans-serif; font-weight: 700; fill: #fff; }
  .brand-name { font-family: "Raleway", sans-serif; font-weight: 700; fill: var(--green-deep); }
  .tagline { font-family: "Open Sans", sans-serif; font-style: italic; font-weight: 700; fill: var(--ink-grey); }
</style>
</head>
<body>
<main class="canvas">
  <article class="cover">
    <svg viewBox="0 0 520 700" xmlns="http://www.w3.org/2000/svg">
      <defs>
        <linearGradient id="roadScene" x1="0" y1="0" x2="1" y2="1">
          <stop offset="0" stop-color="#1a7a3a"/>
          <stop offset=".6" stop-color="#146c33"/>
          <stop offset="1" stop-color="#0d4f25"/>
        </linearGradient>
        <linearGradient id="tankerTone" x1="0" y1="0" x2="1" y2="1">
          <stop offset="0" stop-color="#7c8a80"/>
          <stop offset=".55" stop-color="var(--steel)"/>
          <stop offset="1" stop-color="var(--brick)"/>
        </linearGradient>
        <linearGradient id="hazardTone" x1="0" y1="0" x2="1" y2="1">
          <stop offset="0" stop-color="#e8e4dc"/>
          <stop offset=".6" stop-color="#cfc9bf"/>
          <stop offset="1" stop-color="#c0392b"/>
        </linearGradient>
      </defs>

      <!-- Header panel with road scene -->
      <path class="header-panel" role="img" aria-label="Green-tinted photo of a tanker truck on a road"
            fill="url(#roadScene)"
            d="M0 0 H505 V95 L470 420 Q466 450 436 450 H0 Z"/>

      <!-- Leaf motifs -->
      <path class="leaf leaf-plain" fill="#ffffff"
            d="M80 172 H107 V222 Q107 245 84 245 H57 V195 Q57 172 80 172 Z"/>
      <path class="leaf leaf-photo" role="img" aria-label="Photo of a chrome tanker trailer"
            fill="url(#tankerTone)"
            d="M195 125 H275 V200 Q275 245 230 245 H150 V170 Q150 125 195 125 Z"/>
      <path class="leaf leaf-photo" role="img" aria-label="Photo of a tank shell with a flammable hazard placard"
            fill="url(#hazardTone)"
            d="M82 250 H120 V318 Q120 355 83 355 Q43 355 43 302 Q43 250 82 250 Z"/>

      <!-- Title -->
      <text class="series-label" x="158" y="278" font-size="21">DANGEROUS GOODS</text>
      <text class="book-title" x="156" y="318" font-size="42">TANK</text>

      <!-- Series tabs -->
      <g class="series-tabs" fill="var(--green)">
        <path class="series-tab" d="M58 464 H194 Q201 464 200 471 L189 523 Q188 530 181 530 H45 Q38 530 39 523 L50 471 Q51 464 58 464 Z"/>
        <path class="series-tab" d="M218 464 H354 Q361 464 360 471 L349 523 Q348 530 341 530 H205 Q198 530 199 523 L210 471 Q211 464 218 464 Z"/>
        <path class="series-tab" d="M378 464 H512 Q519 464 518 471 L509 523 Q508 530 501 530 H365 Q358 530 359 523 L370 471 Q371 464 378 464 Z"/>
      </g>

      <!-- Publisher -->
      <rect class="brand-mark" x="455" y="585" width="28" height="28" fill="var(--green-deep)"/>
      <text class="brand-name" x="496" y="638" font-size="12" text-anchor="end">TESSANOR LAB</text>
      <text class="tagline" x="395" y="664" font-size="13" text-anchor="end">Go Forward with Assurance</text>
    </svg>
  </article>
</main>
</body>
</html>
```